Whiskey Bottle Label Design

I need a label made for a short run whiskey bottle that will be given out as gifts.

I want it to look in a vintage style similar to the ones I have attached. I have also attached a file of the information I kind of want on it.

- I would like it on a vintage color label, maybe with a frame/border around it
- Limited edition
- Brackwell is the main title
- Goodwill Cask Reserve
- His signature
- Tennessee Whiskey

I would like to use the following sayings as a small written font (not exactly script like I have pictured, but more like hand writing) just repeating over and over.

"rent is due, pay the man • 2011 Pinehollow Invitational champion • only thing getting in the way is you • 2012 Fair Meadow Cup champion • work hard, play hard • 2014 Harvest Mutual Masters champion • only easy day was yesterday"

I would like the Tennessee tri-star over it but maybe more sketched over it instead of just defined hard stars.

* This label has to look very high end. Also, it needs to be square in design. For colors, use a navy and red/crimson vintage look

```html
<!DOCTYPE html>
<html lang="en">
<head>
<meta charset="utf-8">
<title>Brackwell Tennessee Whiskey Label</title>
<link rel="stylesheet" href="https://fonts.googleapis.com/css2?family=Old+Standard+TT:wght@700&family=Great+Vibes&family=Cinzel:wght@400&family=Montserrat:wght@400&display=swap">
<style>
  :root {
    --backdrop: #000000;
    --gold-deep: #a8782e;
    --gold-mid: #d2a552;
    --gold-light: #f3de86;
    --cream: #ece3c2;
    --cream-dark: #c9b98a;
    --crimson-bright: #a50000;
    --crimson-mid: #6b0608;
    --crimson-dark: #330b0c;
    --ink: #0c0a08;
    --white: #ffffff;
  }
  html, body {
    margin: 0;
    padding: 0;
    width: 1200px;
    height: 1200px;
    overflow: hidden;
    background: var(--backdrop);
  }
  .label-canvas {
    display: block;
    width: 1200px;
    height: 1200px;
  }
  .brand-title {
    font-family: "Old Standard TT", Georgia, serif;
    font-weight: 700;
    font-size: 52px;
    letter-spacing: 2px;
    fill: var(--ink);
  }
  .sayings {
    font-family: "Great Vibes", cursive;
    font-size: 18px;
    fill: var(--gold-mid);
  }
  .edition-text {
    font-family: "Great Vibes", cursive;
    font-size: 27px;
    fill: var(--ink);
  }
  .selection-text {
    font-family: "Montserrat", Arial, sans-serif;
    font-size: 17.5px;
    fill: var(--white);
  }
  .style-text {
    font-family: "Cinzel", Georgia, serif;
    font-size: 19px;
    fill: var(--white);
    letter-spacing: 0.5px;
  }
</style>
</head>
<body>
<svg class="label-canvas" viewBox="0 0 1200 1200" xmlns="http://www.w3.org/2000/svg">
  <defs>
    <linearGradient id="goldFrame" x1="0" y1="0" x2="1" y2="0">
      <stop offset="0" stop-color="var(--gold-deep)"/>
      <stop offset="0.2" stop-color="var(--gold-mid)"/>
      <stop offset="0.45" stop-color="var(--gold-deep)"/>
      <stop offset="0.7" stop-color="var(--gold-light)"/>
      <stop offset="1" stop-color="var(--gold-deep)"/>
    </linearGradient>
    <radialGradient id="crimsonPanel" cx="0.5" cy="0.45" r="0.6">
      <stop offset="0" stop-color="var(--crimson-bright)"/>
      <stop offset="0.55" stop-color="var(--crimson-mid)"/>
      <stop offset="1" stop-color="var(--crimson-dark)"/>
    </radialGradient>
    <radialGradient id="cartoucheFill" cx="0.5" cy="0.25" r="0.7">
      <stop offset="0" stop-color="var(--crimson-bright)"/>
      <stop offset="0.6" stop-color="var(--crimson-mid)"/>
      <stop offset="1" stop-color="var(--crimson-dark)"/>
    </radialGradient>
    <linearGradient id="creamBand" x1="0" y1="0" x2="1" y2="0">
      <stop offset="0" stop-color="var(--cream-dark)"/>
      <stop offset="0.3" stop-color="var(--cream)"/>
      <stop offset="0.7" stop-color="var(--cream)"/>
      <stop offset="1" stop-color="var(--cream-dark)"/>
    </linearGradient>
    <linearGradient id="goldPill" x1="0" y1="0" x2="1" y2="0">
      <stop offset="0" stop-color="#6a4418"/>
      <stop offset="0.45" stop-color="var(--gold-light)"/>
      <stop offset="1" stop-color="#6a4418"/>
    </linearGradient>
    <linearGradient id="bronzePill" x1="0" y1="0" x2="1" y2="0">
      <stop offset="0" stop-color="#3f2510"/>
      <stop offset="0.5" stop-color="#a67c3e"/>
      <stop offset="1" stop-color="#3f2510"/>
    </linearGradient>
    <linearGradient id="goldVertical" x1="0" y1="0" x2="0" y2="1">
      <stop offset="0" stop-color="var(--gold-light)"/>
      <stop offset="1" stop-color="var(--gold-deep)"/>
    </linearGradient>
    <path id="titleArc" d="M428,412 Q600,322 776,412"/>
  </defs>

  <!-- Label frame -->
  <rect class="label-frame" x="343" y="217" width="513" height="765" rx="50" fill="url(#goldFrame)"/>
  <rect class="label-panel" x="359" y="233" width="481" height="733" rx="36" fill="url(#crimsonPanel)"/>

  <!-- Title banner -->
  <path class="title-banner-shadow" d="M395,400 Q500,348 600,345 Q700,348 806,400 L806,462 Q700,412 600,412 Q500,412 395,462 Z" fill="var(--crimson-dark)" opacity="0.7"/>
  <path class="title-banner"
        d="M395,390 Q395,378 410,370 Q500,328 532,322 C534,270 566,252 600,252 C634,252 666,270 668,322 Q700,328 790,370 Q806,378 806,390 L806,440 Q806,455 792,448 Q700,405 600,405 Q500,405 408,448 Q395,455 395,440 Z"
        fill="url(#creamBand)" stroke="url(#goldFrame)" stroke-width="5"/>
  <g class="crown-emblem" role="img" aria-label="Gold crown emblem">
    <rect x="562" y="264" width="76" height="62" rx="6" fill="url(#goldVertical)" opacity="0.9"/>
  </g>
  <text class="brand-title"><textPath href="#titleArc" startOffset="50%" text-anchor="middle">BRACKWELL</textPath></text>

  <!-- Repeating sayings -->
  <g class="sayings" text-anchor="middle">
    <text x="600" y="466">rent is due, pay the man · 2011 Pinehollow Invitational</text>
    <text x="600" y="494">champion · only thing getting in the way is you ·</text>
    <text x="600" y="521">2012 Fair Meadow Cup champion · work hard,</text>
    <text x="600" y="549">play hard · 2014 Harvest Mutual Masters</text>
    <text x="600" y="576">champion · only easy day was yesterday.</text>
    <text x="600" y="604">rent is due, pay the man · 2011 Pinehollow Invitational</text>
    <text x="600" y="632">champion · only thing getting in the way is you ·</text>
    <text x="600" y="659">2012 Fair Meadow Cup champion · work hard,</text>
    <text x="600" y="687">play hard · 2014 Harvest Mutual Masters</text>
    <text x="600" y="714">champion · only easy day was yesterday.</text>
  </g>

  <!-- Edition cartouche -->
  <path class="edition-cartouche"
        d="M470,752 Q470,731 500,731 L700,731 Q730,731 730,752 L752,752 L752,770 Q818,790 818,842 Q818,894 752,914 L752,932 L730,932 Q730,952 700,952 L500,952 Q470,952 470,932 L448,932 L448,914 Q381,894 381,842 Q381,790 448,770 L448,752 Z"
        fill="url(#cartoucheFill)" stroke="url(#goldFrame)" stroke-width="4"/>
  <g class="filigree-left" role="img" aria-label="Gold filigree ornament">
    <rect x="390" y="778" width="88" height="128" rx="40" fill="url(#goldVertical)" opacity="0.55"/>
  </g>
  <g class="filigree-right" role="img" aria-label="Gold filigree ornament">
    <rect x="722" y="778" width="88" height="128" rx="40" fill="url(#goldVertical)" opacity="0.55"/>
  </g>

  <rect class="edition-pill" x="481" y="753" width="238" height="33" rx="16.5" fill="url(#goldPill)" stroke="#5a1410" stroke-width="2"/>
  <text class="edition-text" x="600" y="780" text-anchor="middle">Limited Edition</text>

  <text class="selection-text" x="604" y="816" text-anchor="middle">Goodwill Cask Reserve</text>

  <g class="signature-mark" role="img" aria-label="Handwritten signature">
    <rect x="537" y="829" width="146" height="50" rx="6" fill="var(--gold-mid)" opacity="0.22"/>
  </g>

  <rect class="style-pill" x="481" y="900" width="238" height="32" rx="16" fill="url(#bronzePill)" stroke="var(--gold-mid)" stroke-width="2"/>
  <text class="style-text" x="600" y="924" text-anchor="middle">TENNESSEE WHISKEY</text>
</svg>
</body>
</html>
```